Harbour Vale Lettings Web Site Design

I am after a very simple 3 page web site please. I attach a PDF with the text and information. The logo is also in the PDF. The colours should be orange and blues. The pages should be HOME - LANDLORDS - TENANTS.
Lettings and Property Management Company aimed at just being a reference point for tenants but more of a sales pitch to landlords. Please refer to the attached PDF and word file which contains far more content for the various pages.

Target Market(s)

Prospective Landlords mainly but tenants also

Industry/Entity Type

Lettings and Property Management

Number of Pages Required

3 page

Font styles to use
Sans Serif
Other font styles liked:
• Candara

Colors
0054AA
0677BA
7BADD7
CADEEF
E8F1F8
F0912C
F2A743
F7CA91
FBE8D2
FDF5EE

Requirements
Must have
• Must be colour co-ordinated to the logo (orange and dark blue predominently, Must have good quality stock images relating to property and renting out property. Should have home page and links to landlord page and tenant page. Must have the 4 logos that we are affiliated to (TKR, Tenancy Settle, BNF and Funds Guard Scheme) - all attached.
Nice to have
• Modern feel, crisp and sharp but simple - good stock images.

```html
<!DOCTYPE html>
<html lang="en">
<head>
<meta charset="utf-8">
<title>Harbour Vale Lettings</title>
<link rel="stylesheet" href="https://fonts.googleapis.com/css2?family=Tinos:wght@400;700&family=Montserrat:wght@400;500;700&display=swap">
<style>
  :root {
    --navy: #2a3766;
    --hero-dark: #2f3a5f;
    --hero-light: #46507a;
    --orange: #e5891e;
    --sky: #4aaecd;
    --paper: #f6f6f6;
    --sketch-tone: #e4e4e4;
    --white: #ffffff;
    --ink: #1c1c1c;
    --footer: #003a70;
    --card-line: #d3e4f6;
    --tkr: #7cc242;
    --funds: #5fd38d;
    --settle: #8d4aa8;
    --bnf: #0b3265;
    --serif: "Tinos", "Times New Roman", serif;
    --sans: "Montserrat", Arial, sans-serif;
  }
  * { box-sizing: border-box; margin: 0; padding: 0; }
  html, body { width: 928px; height: 1200px; overflow: hidden; }
  body { position: relative; background: var(--white); font-family: var(--sans); color: var(--ink); }

  .about-band { position: absolute; left: 0; top: 0; width: 928px; height: 899px; background: var(--paper); }

  .hero { position: absolute; left: 0; top: 0; width: 928px; height: 600px; }
  .hero svg { display: block; }

  .top-nav { position: absolute; left: 0; top: 26px; width: 928px; height: 34px; }
  .nav-button {
    position: absolute; top: 0; height: 34px;
    font-family: var(--serif); font-weight: 700; font-size: 12px; letter-spacing: 0.3px;
    color: #111; display: flex; align-items: center; justify-content: center; text-decoration: none;
  }
  .nav-landlords { left: 110px; width: 98px; background: var(--orange); }
  .nav-tenants { left: 734px; width: 88px; background: var(--sky); }
  .hero-tagline {
    position: absolute; left: 0; width: 928px; top: 4px; text-align: center;
    font-family: var(--serif); font-size: 22px; color: var(--white); letter-spacing: 0.3px;
  }

  .brand-mark {
    position: absolute; left: 404px; top: 138px; width: 120px; height: 120px;
    border-radius: 50%; background: var(--orange);
  }
  .brand-name {
    position: absolute; left: 0; width: 928px; top: 284px; text-align: center;
    font-family: var(--serif); font-weight: 400; font-size: 44px; line-height: 44px;
    color: var(--white); letter-spacing: 2px; text-transform: uppercase;
  }
  .brand-name span { display: block; }

  .section-title {
    position: absolute; left: 0; width: 928px; text-align: center;
    font-family: var(--serif); font-weight: 400; font-size: 28px; color: var(--navy);
  }
  .title-rule { position: absolute; left: 437px; width: 54px; height: 2px; background: var(--sky); }

  .about-title { top: 610px; }
  .about-rule { top: 647px; }
  .about-copy {
    position: absolute; left: 120px; width: 688px; text-align: center;
    font-size: 10px; line-height: 19.8px; color: var(--ink);
  }
  .about-copy strong { font-weight: 700; }
  .copy-one { top: 665px; }
  .copy-two { top: 733px; }

  .enquiry-button {
    position: absolute; left: 354px; top: 810px; width: 220px; height: 46px;
    background: var(--sky); color: var(--white); text-align: center; text-decoration: none;
    display: flex; flex-direction: column; justify-content: center;
  }
  .enquiry-button .label { font-weight: 700; font-size: 13px; letter-spacing: 0.2px; }
  .enquiry-button .sub { font-size: 9.5px; margin-top: 2px; }

  .house-sketch {
    position: absolute; left: 675px; top: 794px; width: 253px; height: 102px;
    background: radial-gradient(ellipse 55% 60% at 55% 70%, var(--sketch-tone) 0%, rgba(246,246,246,0) 100%);
  }

  .members-title { top: 942px; }
  .members-rule { top: 981px; }
  .member-row { position: absolute; left: 112px; top: 998px; width: 712px; height: 100px; display: flex; gap: 8px; }
  .member-card {
    flex: 1; background: var(--white); border: 1px solid var(--card-line);
    box-shadow: 0 2px 6px rgba(40, 80, 140, 0.08);
    display: flex; align-items: center; justify-content: center; gap: 8px;
  }
  .member-mark { width: 28px; height: 28px; flex: none; }
  .member-name { font-size: 14px; font-weight: 700; white-space: nowrap; }
  .tkr .member-mark { background: var(--tkr); border-radius: 4px; }
  .tkr .member-name { color: var(--tkr); font-size: 20px; }
  .funds .member-mark { background: var(--funds); border-radius: 50%; }
  .funds .member-name { color: #444; font-weight: 500; font-size: 12px; }
  .settle .member-mark { background: var(--settle); }
  .settle .member-name { color: var(--settle); font-weight: 500; font-size: 14px; }
  .bnf .member-mark { background: var(--bnf); }
  .bnf .member-name { color: var(--bnf); font-size: 20px; }

  .site-footer {
    position: absolute; left: 0; top: 1153px; width: 928px; height: 47px; background: var(--footer);
    color: var(--white); font-size: 9.5px; display: flex; align-items: center; justify-content: center;
  }
</style>
</head>
<body>
  <div class="about-band"></div>

  <header class="hero">
    <svg width="928" height="600" viewBox="0 0 928 600" role="img" aria-label="Photo of a bright modern living room under a dark blue overlay, edged by blue and orange curves">
      <defs>
        <linearGradient id="heroShade" x1="0" y1="0" x2="1" y2="1">
          <stop offset="0" stop-color="#46507a"/>
          <stop offset="0.5" stop-color="#3d4770"/>
          <stop offset="1" stop-color="#2f3a5f"/>
        </linearGradient>
      </defs>
      <path d="M0,368 C150,460 400,555 650,561 C800,564 900,525 928,505 V0 H0 Z" fill="#e5891e"/>
      <path d="M0,368 C150,447 400,527 650,533 C800,535 890,470 928,440 V0 H0 Z" fill="#4aaecd"/>
      <path d="M0,368 C150,440 400,516 650,523 C800,526 890,452 928,412 V0 H0 Z" fill="url(#heroShade)"/>
    </svg>

    <nav class="top-nav">
      <a class="nav-button nav-landlords" href="#">LANDLORDS</a>
      <p class="hero-tagline">LET US MANAGE YOUR PROPERTY</p>
      <a class="nav-button nav-tenants" href="#">TENANTS</a>
    </nav>

    <div class="brand-mark"></div>
    <h1 class="brand-name"><span>Harbour Vale</span><span>Lettings</span></h1>
  </header>

  <section class="about">
    <h2 class="section-title about-title">ABOUT US</h2>
    <div class="title-rule about-rule"></div>
    <p class="about-copy copy-one"><strong>Harbour Vale Lettings</strong> has emerged after over 20 years of privately managing our own rental properties. We are family run and decided to move all of our properties under one ‘umbrella’. Now professionally set up as a legal entity, Harbour Vale is looking to welcome new tenants and landlords to an innovative and fresh way of letting property.</p>
    <p class="about-copy copy-two">We always maintain a high standard of service and our friendly and helpful team are experienced in all areas and offer an excellent service in helping landlords and tenants deal with problems and issues they face daily. Out of hours emergency service which means we are there (in an emergency) for our tenants and landlords 24/7.</p>
    <a class="enquiry-button" href="#">
      <span class="label">LANDLORD ENQUIRY</span>
      <span class="sub">Actively Looking for new landlords</span>
    </a>
    <div class="house-sketch" role="img" aria-label="Line sketch of a detached house with trees and birds"></div>
  </section>

  <section class="members">
    <h2 class="section-title members-title">WE ARE MEMBERS OF</h2>
    <div class="title-rule members-rule"></div>
    <div class="member-row">
      <div class="member-card tkr"><span class="member-mark"></span><span class="member-name">TKR</span></div>
      <div class="member-card funds"><span class="member-mark"></span><span class="member-name">Funds Guard Scheme</span></div>
      <div class="member-card settle"><span class="member-mark"></span><span class="member-name">Tenancy Settle</span></div>
      <div class="member-card bnf"><span class="member-mark"></span><span class="member-name">BNF</span></div>
    </div>
  </section>

  <footer class="site-footer">© 2025 Harbour Vale Letting Property Management. All Rights Reserved.</footer>
</body>
</html>
```